Flyer Improve For Painting Company

Flyer Improve layout for painting company, attached.

Super Action Hero improve in flyer.

Flyer we are testing success with (entertainment) and Super Action Hero or Dog, no job photos.

Name of Super Action Hero or Dog.

Colours are up to your creativity.

Flyer size make A4, single sided flyer only.

Keep print format, set out tidy up.

Flyer make WOW to attract customers to hire our painting services.

Kind Regards

Mark

```html
<!DOCTYPE html>
<html lang="en">
<head>
<meta charset="utf-8">
<title>Brightcoat Painting Flyer</title>
<link rel="stylesheet" href="https://fonts.googleapis.com/css2?family=Open+Sans:ital,wght@0,400;0,700;1,300&family=Carlito:wght@400;700&display=swap">
<style>
  :root {
    --brand-orange: #d9502c;
    --accent-cyan: #3ec6d3;
    --heading-yellow: #fde27a;
    --paper: #ffffff;
    --ink-light: #ffffff;
    --dog-light: #efe9e2;
    --dog-tone: #c98a52;
  }
  * { margin: 0; padding: 0; box-sizing: border-box; }
  html, body { width: 848px; height: 1200px; overflow: hidden; background: var(--paper); }
  .flyer {
    position: relative;
    width: 848px;
    height: 1200px;
    overflow: hidden;
    background: var(--paper);
    font-family: "Carlito", "Calibri", sans-serif;
    color: var(--ink-light);
  }
  .abs { position: absolute; }

  .brand { left: 68px; top: 34px; color: var(--brand-orange); }
  .brand-name { font-family: "Open Sans", sans-serif; font-weight: 700; font-size: 54px; line-height: 62px; letter-spacing: -0.5px; }
  .brand-tagline { font-family: "Open Sans", sans-serif; font-weight: 400; font-size: 25px; line-height: 30px; margin-top: -2px; }

  .headline-band { left: 46px; top: 248px; width: 440px; height: 156px; }
  .headline {
    left: 86px; top: 252px;
    font-family: "Open Sans", sans-serif; font-style: italic; font-weight: 300;
    font-size: 66px; line-height: 68px; color: var(--ink-light);
  }
  .headline .line-two { display: block; padding-left: 76px; }

  .paint-field { left: 0; top: 0; width: 848px; height: 1200px; }

  .mascot-photo { left: 486px; top: 88px; width: 330px; height: 498px; }

  .section-title { font-family: "Carlito", sans-serif; font-weight: 700; font-size: 25px; color: var(--heading-yellow); letter-spacing: 0.3px; }
  .services { left: 62px; top: 596px; }
  .services ul { list-style: none; margin-top: 6px; }
  .services li { font-weight: 700; font-size: 16.5px; line-height: 25.5px; }

  .ideals { left: 58px; top: 726px; }
  .ideals ul { list-style: none; margin-top: 4px; }
  .ideals li { font-size: 16.5px; line-height: 21.3px; }
  .ideals b { font-weight: 700; }

  .contact { left: 60px; top: 896px; font-size: 13.3px; line-height: 20px; }
  .contact b { font-weight: 700; }
  .contact .gap { height: 12px; }

  .voucher-band { left: 48px; top: 1080px; width: 320px; height: 66px; }
  .voucher { left: 74px; top: 1086px; display: flex; align-items: center; color: var(--brand-orange); }
  .voucher-amount { font-weight: 700; font-size: 42px; line-height: 50px; margin-right: 10px; }
  .voucher-text { font-size: 15px; line-height: 15px; }
  .voucher-text small { display: block; font-size: 10px; line-height: 11px; }
  .voucher-text em { display: block; font-size: 9.5px; line-height: 10px; }

  .cut-line { left: 392px; top: 890px; width: 456px; height: 310px; }

  .coupon { left: 418px; top: 902px; width: 400px; font-size: 10.6px; line-height: 17px; font-weight: 700; }
  .coupon-title { font-size: 17.5px; line-height: 22px; padding-left: 18px; margin-bottom: 8px; }
  .check-row { display: flex; align-items: center; gap: 8px; margin-bottom: 13px; }
  .check-row .option { display: flex; align-items: center; gap: 8px; margin-right: 10px; }
  .checkbox { width: 10px; height: 10px; background: var(--paper); display: inline-block; }
  .coupon-fields { padding-left: 18px; line-height: 16.5px; }
  .coupon-fields .spaced { margin-top: 4px; }
  .dots { font-weight: 400; letter-spacing: 0.4px; }
</style>
</head>
<body>
<main class="flyer">

  <svg class="abs paint-field" viewBox="0 0 848 1200" aria-hidden="true">
    <polygon fill="var(--brand-orange)" points="0,1200 0,478 12,470 24,477 38,466 52,474 66,463 80,472 96,462 112,471 128,460 144,470 160,462 176,472 192,476 210,470 228,484 246,478 264,490 282,484 300,494 318,488 336,498 354,494 366,520 372,540 388,532 404,540 420,534 436,548 448,556 458,582 474,586 490,580 506,592 522,588 540,600 556,606 566,624 576,652 588,680 604,690 620,682 640,692 660,684 680,692 700,684 720,690 740,680 760,688 780,678 800,686 820,678 836,684 848,678 848,1200"/>
  </svg>

  <header class="abs brand">
    <div class="brand-name">Brightcoat</div>
    <div class="brand-tagline">Proffesional Painting</div>
  </header>

  <svg class="abs headline-band" viewBox="0 0 440 156" aria-hidden="true">
    <polygon fill="var(--accent-cyan)" points="8,4 60,0 140,3 230,0 330,2 410,0 424,6 420,40 426,70 380,74 392,82 436,86 440,120 432,150 360,156 260,152 160,156 100,150 102,120 96,92 40,88 6,84 2,50 6,20"/>
  </svg>
  <h1 class="abs headline">Confidence<span class="line-two">in colour</span></h1>

  <svg class="abs mascot-photo" viewBox="0 0 330 498" role="img" aria-label="Photo of a small white and tan Jack Russell terrier standing and facing forward, the company's mascot">
    <defs>
      <radialGradient id="mascotTone" cx="50%" cy="45%" r="60%">
        <stop offset="0%" stop-color="var(--dog-light)"/>
        <stop offset="100%" stop-color="var(--dog-tone)" stop-opacity="0.55"/>
      </radialGradient>
    </defs>
    <rect width="330" height="498" rx="40" fill="url(#mascotTone)"/>
  </svg>

  <section class="abs services">
    <h2 class="section-title">OUR SERVICES</h2>
    <ul>
      <li>Residential Interior &amp; Exterior painting</li>
      <li>Commercial painting by delivering peace of mind with superior</li>
      <li>Workmanship, finishes and service</li>
    </ul>
  </section>

  <section class="abs ideals">
    <h2 class="section-title">OUR IDEALS</h2>
    <ul>
      <li><b>Professionalism:</b> Highly-experienced painters</li>
      <li><b>Clean:</b> No mess! we respect your property and clean-up after ourselves.</li>
      <li><b>Trustworthy:</b> We are there until we see the smile on your face!</li>
      <li><b>Responsible:</b> “Set us and forget us”</li>
      <li><b>Reliable:</b> On time, or we will pay you $100 for each day we’re late</li>
    </ul>
  </section>

  <address class="abs contact" style="font-style:normal">
    <div><b>Countrywide Wide Service</b></div>
    <div>Brightcoat Proffesional Painting</div>
    <div><b>Free call today</b> 1800 555 274</div>
    <div><b>Fax</b> 03 9555 0142</div>
    <div><b>Email:</b> paint@brightcoat.com.au</div>
    <div class="gap"></div>
    <div>Book your job today. Limited sale time! Hurry!</div>
    <div><b>Call us today</b> 0400 555 819</div>
    <div><b>Book online now at:</b> www.brightcoat.com.au</div>
  </address>

  <svg class="abs voucher-band" viewBox="0 0 320 66" aria-hidden="true">
    <polygon fill="var(--paper)" points="6,6 40,2 120,4 200,0 280,3 314,2 318,20 312,34 320,50 314,64 240,62 160,66 80,62 20,64 4,58 10,44 0,30 8,18"/>
  </svg>
  <div class="abs voucher">
    <div class="voucher-amount">$100</div>
    <div class="voucher-text">
      Free gift voucher off your job
      <small>Download at <b>www.brightcoat.com.au</b></small>
      <em>One only per customer</em>
    </div>
  </div>

  <svg class="abs cut-line" viewBox="0 0 456 310" aria-hidden="true">
    <line x1="8" y1="0" x2="380" y2="0" stroke="var(--ink-light)" stroke-width="1.2" stroke-dasharray="10 8" transform="translate(0,2)"/>
    <line x1="2" y1="6" x2="2" y2="310" stroke="var(--ink-light)" stroke-width="1.2" stroke-dasharray="10 8"/>
    <g transform="translate(392,-8)" stroke="var(--ink-light)" stroke-width="2" fill="none">
      <circle cx="26" cy="4" r="5"/>
      <circle cx="26" cy="16" r="5"/>
      <line x1="21" y1="6" x2="0" y2="14"/>
      <line x1="21" y1="14" x2="0" y2="6"/>
    </g>
  </svg>

  <section class="abs coupon">
    <h2 class="coupon-title">FREE EASY COUPON:</h2>
    <div class="check-row"><span class="checkbox"></span> Yes please visit and give us a quote( Valued at $147) Yours FREE!</div>
    <div class="check-row">
      <span class="option"><span class="checkbox"></span> Internal painting</span>
      <span class="option"><span class="checkbox"></span> External painting</span>
      <span class="option"><span class="checkbox"></span> Handyman</span>
      <span class="option" style="margin-left:14px">Building</span>
    </div>
    <div class="coupon-fields">
      <div>Jobs I want done are<span class="dots">.............................................................................</span></div>
      <div><span class="dots">............................................................................................................</span></div>
      <div>Visit time best preferred time<span class="dots">.................</span>day<span class="dots">................</span>month<span class="dots">................</span>2013</div>
      <div>Mail coupon to: Brightcoat P.O Box 482 Millbrook Vic 3999</div>
      <div>Name<span class="dots">...................................................................................................</span></div>
      <div>Address<span class="dots">..............................................................................................</span></div>
      <div>Suburb<span class="dots">.............................</span>P/Code<span class="dots">.............................</span>Phone<span class="dots">.............................</span></div>
      <div>Email<span class="dots">............................</span></div>
      <div>Want to talk 24 hours leave a message call now on 1800 555 274</div>
      <div>Email or fax FREE EAST COUPON to: paint@brightcoat.com.au Fax 03 9555 0142</div>
    </div>
  </section>

</main>
</body>
</html>
```